Business Card Design Project

Our slogan is "FIND YOUR OWN TRAIL" and we are after something creative and different to go with our company image.

Criteria:
The business card will not be a standard size but it must be small or big enough to fit in a wallet.
It will be double sided
It will have our colours and the design will be based around our logo (attached)
No fancy text just clean sharp easy to read. we have been using the stag sans book font type so this or similar type is preferable (we are not locked in a font type.

For more information about us, please visit out website at www.glimtrovale.com.au

Target Market(s)

outdoor and recreational industry/market

Industry/Entity Type

Business

Requirements
Must have
• Logo
Slogan
website
contact details (phone and email)
Name and Position
social media facebook and youtube

```html
<!DOCTYPE html>
<html lang="en">
<head>
<meta charset="utf-8">
<title>Glimtrovale Business Card</title>
<link rel="stylesheet" href="https://fonts.googleapis.com/css2?family=Montserrat:wght@300;400;500&display=swap">
<style>
  :root {
    --backdrop: #e8e3dc;
    --card-center: #2c2c2e;
    --card-edge: #19191a;
    --accent: #e0542a;
    --ink-light: #f2f2f2;
    --ink-muted: #b9b9b9;
  }
  * { margin: 0; padding: 0; box-sizing: border-box; }
  html, body {
    width: 1200px; height: 1200px; overflow: hidden;
    background: var(--backdrop);
    font-family: "Montserrat", Arial, sans-serif;
  }
  .canvas { position: relative; width: 1200px; height: 1200px; }
  .card {
    position: absolute; top: 418px;
    width: 312px; height: 366px; overflow: hidden;
    background: radial-gradient(ellipse at 50% 40%, var(--card-center), var(--card-edge) 80%);
    box-shadow: 0 6px 18px rgba(0,0,0,0.25);
  }
  .card--front { left: 148px; }
  .card--back { left: 732px; }

  /* front */
  .front-ring { position: absolute; left: 100px; top: 98px; width: 100px; height: 100px; }
  .front-wordmark {
    position: absolute; left: 0; right: 0; top: 228px; text-align: center;
    color: var(--ink-light); font-weight: 300; font-size: 23px; letter-spacing: 3px;
  }
  .front-slogan {
    position: absolute; left: 0; right: 0; top: 264px; text-align: center;
    color: var(--ink-light); font-weight: 500; font-size: 8px; letter-spacing: 3px;
  }

  /* back */
  .holder-name {
    position: absolute; left: 28px; top: 50px;
    color: var(--accent); font-weight: 400; font-size: 13px;
  }
  .holder-role {
    position: absolute; left: 28px; top: 69px;
    color: var(--ink-muted); font-weight: 300; font-size: 8px;
  }
  .contact-list { position: absolute; left: 58px; top: 116px; list-style: none; }
  .contact-item {
    display: flex; align-items: center; height: 14px;
    color: var(--ink-muted); font-size: 7px; font-weight: 300;
  }
  .contact-icon { width: 10px; height: 10px; margin-right: 6px; flex: none; }
  .side-brand {
    position: absolute; left: 250px; top: 168px;
    transform-origin: 0 0; transform: rotate(-90deg);
    white-space: nowrap;
  }
  .side-wordmark {
    display: block; color: var(--ink-light); font-weight: 300;
    font-size: 19px; letter-spacing: 2px; line-height: 24px;
  }
  .side-slogan {
    display: block; color: var(--ink-light); font-weight: 500;
    font-size: 7px; letter-spacing: 2.8px; line-height: 12px;
  }
  .back-ring { position: absolute; left: 120px; top: 180px; width: 264px; height: 264px; }
</style>
</head>
<body>
<main class="canvas">
  <section class="card card--front" aria-label="Card front">
    <svg class="front-ring" viewBox="0 0 100 100" aria-hidden="true">
      <circle cx="50" cy="50" r="47" fill="none" stroke="var(--accent)" stroke-width="3"/>
    </svg>
    <p class="front-wordmark">GLIMTROVALE</p>
    <p class="front-slogan">FIND YOUR OWN TRAIL</p>
  </section>

  <section class="card card--back" aria-label="Card back">
    <p class="holder-name">Martin Hale</p>
    <p class="holder-role">Manager</p>
    <ul class="contact-list">
      <li class="contact-item">
        <svg class="contact-icon" viewBox="0 0 10 10" aria-hidden="true"><rect width="10" height="10" rx="2" fill="var(--accent)"/><path d="M3 2.5c-.5.5-.5 1.5.5 3s2 2.3 3 2l.6-.8-1.2-.9-.6.5c-.6-.3-1.1-.9-1.4-1.4l.5-.6-.9-1.2z" fill="var(--card-edge)"/></svg>
        5510 2296
      </li>
      <li class="contact-item">
        <svg class="contact-icon" viewBox="0 0 10 10" aria-hidden="true"><rect width="10" height="10" rx="2" fill="var(--accent)"/><rect x="2" y="3" width="6" height="4.2" fill="none" stroke="var(--card-edge)" stroke-width=".8"/><path d="M2 3l3 2.3L8 3" fill="none" stroke="var(--card-edge)" stroke-width=".8"/></svg>
        martinhale@glimtrovale.com.au
      </li>
      <li class="contact-item">
        <svg class="contact-icon" viewBox="0 0 10 10" aria-hidden="true"><rect width="10" height="10" rx="2" fill="var(--accent)"/><circle cx="5" cy="5" r="2.8" fill="none" stroke="var(--card-edge)" stroke-width=".7"/><path d="M2.2 5h5.6M5 2.2v5.6" stroke="var(--card-edge)" stroke-width=".6"/></svg>
        https://www.glimtrovale.com.au/
      </li>
      <li class="contact-item">
        <svg class="contact-icon" viewBox="0 0 10 10" aria-hidden="true"><rect width="10" height="10" rx="2" fill="var(--accent)"/></svg>
        https://social.glimtrovale.com.au/team
      </li>
    </ul>
    <div class="side-brand">
      <span class="side-wordmark">GLIMTROVALE</span>
      <span class="side-slogan">FIND YOUR OWN TRAIL</span>
    </div>
    <svg class="back-ring" viewBox="0 0 264 264" aria-hidden="true">
      <circle cx="132" cy="132" r="128" fill="none" stroke="var(--accent)" stroke-width="4"/>
    </svg>
  </section>
</main>
</body>
</html>
```